Townhome Multi-Family Property Exterior Sign

Hello. We are looking for a new design for our exterior pylon for for a multi-family housing property in Texas. The design will need to go on a new sign panel to replace the existing (see photo of existing). We are looking to see both modern and contemporary designs. Included the sign should be the name, Loma Brisa Townhomes and the web address www.lomabrisatownhomes.example.

Attached here is a PDF file of the proposed new sign shape. We are open to other shape ideas as well if your design would better suit a more rectangular shape.

Industry/Entity Type

Property

Font styles to use
Serif
Sans Serif

Colors
9bcb3c

Requirements
Must have
• Name of building: Loma Brisa Townhomes
• Website: www.lomabrisatownhomes.example
Nice to have
• Address: 420-530 Halvorsen Lane (only if it fits nicely)

```html
<!DOCTYPE html>
<html lang="en">
<head>
<meta charset="utf-8">
<title>Loma Brisa Townhomes – Exterior Sign</title>
<link rel="stylesheet" href="https://fonts.googleapis.com/css2?family=Archivo+Black&family=Roboto:wght@400;500&family=Roboto+Condensed:wght@400;700&display=swap">
<style>
  :root {
    --backdrop: #efeae2;
    --panel: #ffffff;
    --post: #006f3a;
    --brand-green: #9bcb3c;
    --deep-green: #0b6b35;
    --deep-green-light: #2f8a4c;
    --silver-dark: #a9a9a9;
    --silver-light: #f4f4f4;
    --city-grey: #8a8a8a;
    --white: #ffffff;
  }
  * { margin: 0; padding: 0; box-sizing: border-box; }
  html, body { width: 1200px; height: 854px; overflow: hidden; background: var(--backdrop); }
  .canvas { position: relative; width: 1200px; height: 854px; }
  .sign-art { position: absolute; inset: 0; }
  .brand-name {
    position: absolute; left: 0; width: 1200px; top: 222px;
    text-align: center; font-family: "Archivo Black", sans-serif;
    font-size: 104px; line-height: 1; letter-spacing: 2px; color: var(--brand-green);
  }
  .property-name {
    position: absolute; left: 0; width: 1200px; top: 346px;
    text-align: center; font-family: "Archivo Black", sans-serif;
    font-size: 55px; line-height: 1; letter-spacing: 3px;
    background: linear-gradient(180deg, var(--deep-green-light), var(--deep-green) 60%);
    -webkit-background-clip: text; background-clip: text; color: transparent;
  }
  .property-url {
    position: absolute; left: 0; width: 1200px; top: 410px;
    text-align: center; font-family: "Roboto Condensed", sans-serif;
    font-size: 33px; line-height: 1; color: var(--deep-green);
  }
  .property-url strong { font-weight: 700; }
  .address {
    position: absolute; right: 216px; top: 532px; text-align: right;
    font-family: "Roboto", sans-serif; font-weight: 400; color: var(--white); line-height: 1;
  }
  .address-number { font-size: 36px; display: flex; align-items: center; justify-content: flex-end; gap: 10px; margin-right: -40px; }
  .address-street { font-size: 36px; margin-top: 12px; }
  .pin-icon { width: 30px; height: 30px; }
</style>
</head>
<body>
<div class="canvas">
  <svg class="sign-art" width="1200" height="854" viewBox="0 0 1200 854">
    <defs>
      <linearGradient id="silverBand" x1="0" y1="0" x2="1" y2="0">
        <stop offset="0" stop-color="var(--silver-dark)"/>
        <stop offset="0.5" stop-color="var(--silver-light)"/>
        <stop offset="1" stop-color="var(--silver-dark)"/>
      </linearGradient>
      <linearGradient id="cityTone" x1="0" y1="0" x2="0" y2="1">
        <stop offset="0" stop-color="#b5b5b5"/>
        <stop offset="1" stop-color="var(--city-grey)"/>
      </linearGradient>
    </defs>
    <!-- posts -->
    <g class="post post-left" fill="var(--post)">
      <polygon points="82,282 114,266 146,282"/>
      <rect x="90" y="280" width="48" height="392"/>
    </g>
    <g class="post post-right" fill="var(--post)">
      <polygon points="1054,278 1086,262 1118,278"/>
      <rect x="1062" y="276" width="48" height="396"/>
    </g>
    <!-- panel -->
    <path class="panel" fill="var(--panel)" d="M136,300 C260,290 360,240 440,212 C520,186 680,186 760,212 C840,240 940,296 1064,304 L1064,628 L136,628 Z"/>
    <!-- skyline illustration area -->
    <g role="img" aria-label="Grey city skyline illustration with buildings and clouds">
      <path fill="url(#cityTone)" opacity="0.75" d="M160,548 L190,528 L250,522 L260,500 L400,482 L410,480 L500,488 L560,510 L592,552 L500,604 L300,612 L160,560 Z"/>
    </g>
    <!-- silver swoosh and green wave -->
    <path class="silver-band" fill="url(#silverBand)" d="M136,540 C250,592 330,612 400,604 C560,584 760,470 900,468 C990,468 1040,494 1064,508 L1064,532 C1040,515 980,494 900,492 C760,490 560,590 400,612 C330,620 250,600 136,548 Z"/>
    <path class="green-wave" fill="var(--brand-green)" d="M136,548 C250,600 330,620 400,612 C560,590 760,490 900,492 C980,494 1040,515 1064,532 L1064,628 L136,628 Z"/>
  </svg>

  <div class="brand-name">VELA</div>
  <div class="property-name">LOMA BRISA TOWNHOMES</div>
  <div class="property-url">www.<strong>lomabrisatownhomes</strong>.example</div>

  <div class="address">
    <div class="address-number">420-530
      <svg class="pin-icon" viewBox="0 0 30 30" aria-hidden="true">
        <circle cx="15" cy="15" r="13" fill="none" stroke="var(--white)" stroke-width="2"/>
        <path d="M15 7 a5.5 5.5 0 0 1 5.5 5.5 c0 4-5.5 10-5.5 10 s-5.5-6-5.5-10 A5.5 5.5 0 0 1 15 7 Z" fill="var(--white)"/>
        <circle cx="15" cy="12.5" r="2" fill="var(--brand-green)"/>
      </svg>
    </div>
    <div class="address-street">HALVORSEN LANE</div>
  </div>
</div>
</body>
</html>
```